website design for a new age Real Estate Security Business

We are launching a business in real estate which no body else is doing. We are going to use technology in terms of software and hardware to provide our services.

We are going to use Big Data, IOT etc.. for our services.

NOTE: We don't want to see Shiel or buildings etc.. that directly suggests Real estate or security on this design

Target Market(s)

India

Industry/Entity Type

Real Estate

Number of Pages Required

4 page

Font styles to use
Sans Serif
Other font styles liked:
• Use Google Fonts

Requirements
Must have
• Home Page should be trendy and colourful should give user confidence to subscribe to our service.
Nice to have
• Use Google fonts.
Should not have
• Design shouldnt have Veritas Grid or Buildings that directly suggests real estate or security.

```html
<!DOCTYPE html>
<html lang="en">
<head>
<meta charset="utf-8">
<title>Veritas Grid</title>
<link href="https://fonts.googleapis.com/css2?family=Roboto:wght@300;400;500;700&family=Roboto+Condensed:wght@400;700&display=swap" rel="stylesheet">
<style>
:root{
  --navy:#0a1422;
  --hero-deep:#061020;
  --hero-glow:#1d4f8e;
  --accent-blue:#1f8fe0;
  --accent-red:#d8252b;
  --teal:#7fd0c3;
  --ink:#222;
  --muted:#555;
  --light:#f4f4f4;
  --footer:#16232f;
  --footer-bar:#0f4f8c;
  --std:#f7b500;
  --std-soft:#fbe3a0;
  --std-ink:#c98a00;
  --pre:#13874c;
  --pre-soft:#6aa51a;
  --adv:#0e3457;
  --adv-soft:#4ea7e6;
}
*{box-sizing:border-box;margin:0;padding:0}
html,body{width:1200px;height:2913px;overflow:hidden}
body{position:relative;font-family:'Roboto',sans-serif;color:var(--ink);background:#fff}
.abs{position:absolute}

/* hero */
.hero{left:0;top:0;width:1200px;height:550px;background:radial-gradient(ellipse at 50% 40%,var(--hero-glow) 0%,#0b2346 35%,var(--hero-deep) 75%);border-top:5px solid var(--accent-blue);border-bottom:4px solid var(--accent-red)}
.navbar{left:0;top:5px;width:1200px;height:76px;border-bottom:1px solid rgba(255,255,255,.12)}
.logo{left:160px;top:28px;font-family:'Roboto',sans-serif;font-weight:500;font-size:31px;color:#fff;letter-spacing:.5px}
.nav a{position:absolute;top:40px;color:#fff;font-size:13px;font-weight:500;text-decoration:none;letter-spacing:.5px}
.what{left:404px;top:128px;width:392px;height:43px;background:var(--teal);color:#0b1b2c;font-size:31px;font-weight:500;text-align:center;line-height:43px}
.tree{left:400px;top:171px;width:400px;height:70px}
.feature{top:241px;width:198px;height:171px;background:rgba(20,8,10,.85);border:2px solid #5a1a1a;text-align:center;padding:20px 14px 0}
.feature h3{color:#ff2b2b;font-size:25px;font-weight:500;margin-bottom:14px}
.feature p{color:#fff;font-size:10.5px;line-height:13px}
.feature-icon{top:398px;width:40px;height:40px}
.arrow{top:280px;width:34px;height:34px;border-radius:50%;background:#8a8f96}

/* about */
.about{left:0;top:554px;width:1200px;height:384px;background:linear-gradient(180deg,#e9ebee,#d9dde2)}
.sec-title{width:1200px;text-align:center;font-weight:500;font-size:40px;color:#111}
.rule{left:486px;width:228px;height:2px}
.rule span{position:absolute;top:0;height:2px}
.about-photo{left:161px;top:674px;width:359px;height:225px;border:3px solid #fff;background:linear-gradient(135deg,#c9ccd0,#8a8f97 60%,#5f6670)}
.about-text{left:544px;top:676px;width:392px;font-size:13.5px;line-height:20px;color:#333}
.about-text p+p{margin-top:10px}

/* services */
.svc-photo{background:linear-gradient(135deg,#dfe7ee,#9fb1c2 60%,#5e6e80)}
.svc-land{background:linear-gradient(180deg,#8fb4dc 0%,#cfe0ef 35%,#6e86a0 52%,#5f7a3a 62%,#7c8c4a 100%)}
.svc-card{background:var(--accent-blue);color:#fff;padding:28px 20px 0;box-shadow:0 12px 18px -8px rgba(0,0,0,.35)}
.svc-card .kicker{font-size:17px;font-weight:300;letter-spacing:.3px}
.svc-card h3{font-family:'Roboto Condensed',sans-serif;font-size:37px;font-weight:700;line-height:40px;display:flex;align-items:center;gap:10px}
.svc-card h3 i{flex:1;height:2px;background:#fff;margin-left:8px}
.svc-card p{font-size:10.5px;line-height:15px;margin-top:18px}
.buy{display:flex;align-items:center;margin-top:34px;font-size:13px;gap:10px}
.qty{width:38px;height:24px;border:1px solid #fff;font-size:11px;line-height:22px;padding-left:6px}
.cart{height:30px;background:#0e3d68;padding:0 14px;display:flex;align-items:center;gap:8px;font-size:12px}

/* pricing */
.pricing{left:0;top:1870px;width:1200px;height:631px;background:#f6f6f6;border-top:2px solid #ddd}
.sub{width:1200px;text-align:center;font-size:13px;color:#444}
.plan{top:2012px;width:258px;height:454px;background:#efefef}
.plan-head{height:64px;color:#fff;font-size:24px;font-weight:500;text-align:center;line-height:64px}
.plan-price{height:142px;text-align:center;line-height:130px;font-size:38px;font-weight:700;border-bottom-left-radius:100% 45%;border-bottom-right-radius:0}
.plan-price small{font-size:26px;font-weight:500}
.plan ul{list-style:none;padding:14px 0 0 20px}
.plan li{height:30px;font-size:14.5px;color:#333;display:flex;align-items:center;gap:12px}
.signup{position:absolute;left:50%;transform:translateX(-50%);top:425px;width:98px;height:26px;color:#fff;font-size:12px;text-align:center;line-height:26px}

/* footer */
.footer{left:0;top:2501px;width:1200px;height:369px;background:linear-gradient(180deg,#1c2a37,#121d27)}
.contact{top:2534px;height:68px;border:1px solid rgba(255,255,255,.3);display:flex;align-items:center;color:#fff;font-size:13.5px;line-height:17px}
.contact .ico{width:40px;height:40px;background:#4aa3df;margin:0 14px 0 -1px;display:flex;align-items:center;justify-content:center}
.f-h{top:2642px;color:#fff;font-size:19px;font-weight:400;letter-spacing:.3px}
.f-about{left:161px;top:2676px;width:290px;color:#ddd;font-size:11.5px;line-height:16px}
.f-about a{display:block;margin-top:14px;color:#4aa3df;text-decoration:none}
.f-links{left:565px;top:2676px;list-style:none}
.f-links li{height:27px;color:#fff;font-size:12px}
.f-links li:first-child{color:#4aa3df}
.email{left:837px;top:2680px;width:198px;height:41px;background:#e3e3e3;color:#888;font-size:11.5px;padding-left:12px;line-height:41px}
.subscribe{left:837px;top:2738px;width:96px;height:28px;background:#1f8fe0;color:#fff;font-size:12px;font-weight:700;text-align:center;line-height:28px}
.social{top:2803px;width:30px;height:30px;border-radius:50%;background:#4b5866}
.copy{left:0;top:2870px;width:1200px;height:43px;background:var(--footer-bar);color:#fff;font-size:11px;text-align:center;line-height:43px}
</style>
</head>
<body>

<header class="abs hero" role="img" aria-label="Dark blue data network visualisation with spotlights"></header>
<div class="abs navbar">
  <div class="abs logo">VERITAS GRID</div>
  <nav class="nav">
    <a style="left:632px">HOME</a>
    <a style="left:720px">SERVICES</a>
    <a style="left:850px">PRICING</a>
    <a style="left:966px">CONTACT US</a>
  </nav>
</div>

<div class="abs what">WHAT WE DO?</div>
<svg class="abs tree" viewBox="0 0 400 70" fill="none" stroke="#cfd6de" stroke-width="1.5">
  <line x1="200" y1="0" x2="200" y2="34"/><line x1="5" y1="34" x2="395" y2="34"/>
  <line x1="5" y1="34" x2="5" y2="70"/><line x1="200" y1="34" x2="200" y2="70"/><line x1="395" y1="34" x2="395" y2="70"/>
</svg>

<section class="abs feature" style="left:208px"><h3>DATA</h3><p>Lorem Ipsum is simply dummy text of the printing and typesetting industry. Lorem Ipsum has been the industry's standard</p></section>
<section class="abs feature" style="left:499px"><h3>ANALYSIS</h3><p>Lorem Ipsum is simply dummy text of the printing and typesetting industry. Lorem Ipsum has been the industry's standard</p></section>
<section class="abs feature" style="left:792px"><h3>ACTION</h3><p>Lorem Ipsum is simply dummy text of the printing and typesetting industry. Lorem Ipsum has been the industry's standard</p></section>

<svg class="abs feature-icon" style="left:287px" viewBox="0 0 40 40"><g fill="#fff"><ellipse cx="20" cy="13" rx="8" ry="3"/><rect x="12" y="14" width="16" height="4"/><rect x="12" y="19" width="16" height="4"/><rect x="12" y="24" width="16" height="4"/></g></svg>
<svg class="abs feature-icon" style="left:578px" viewBox="0 0 40 40"><g fill="none" stroke="#fff" stroke-width="2"><rect x="10" y="11" width="20" height="14"/><line x1="20" y1="25" x2="20" y2="30"/><line x1="14" y1="30" x2="26" y2="30"/><circle cx="19" cy="18" r="3"/></g></svg>
<svg class="abs feature-icon" style="left:873px" viewBox="0 0 40 40"><g fill="none" stroke="#fff" stroke-width="2"><rect x="12" y="12" width="12" height="16" transform="rotate(-12 18 20)"/><rect x="17" y="11" width="12" height="16"/></g></svg>

<svg class="abs arrow" style="left:16px" viewBox="0 0 34 34"><circle cx="17" cy="17" r="17" fill="#7b8088"/><path d="M20 10 L13 17 L20 24" fill="none" stroke="#0a1422" stroke-width="3"/></svg>
<svg class="abs arrow" style="left:1149px" viewBox="0 0 34 34"><circle cx="17" cy="17" r="17" fill="#7b8088"/><path d="M14 10 L21 17 L14 24" fill="none" stroke="#0a1422" stroke-width="3"/></svg>

<section class="abs about" role="img" aria-label="Faint grey business charts background"></section>
<h2 class="abs sec-title" style="top:580px">SHORTLY ABOUT VERITAS GRID</h2>
<div class="abs rule" style="top:640px"><span style="left:0;width:228px;background:#bbb"></span><span style="left:84px;width:60px;background:var(--accent-red)"></span></div>
<div class="abs about-photo" role="img" aria-label="Photo of a man on the phone at an office desk with a computer"></div>
<div class="abs about-text">
  <p>Lorem Ipsum is simply dummy text of the printing and typesetting industry. Lorem Ipsum has been the industry's standard dummy text ever since the 1500s, when an unknown printer took a galley of type and scrambled it to make a type specimen book. It has survived not only five centuries, but also the leap into electronic typesetting, remaining essentially unchanged.</p>
  <p>Lorem Ipsum is simply dummy text of the printing and typesetting industry. Lorem Ipsum has been the industry's standard dummy text ever since the 1500s...</p>
</div>

<h2 class="abs sec-title" style="top:976px">SERVICES</h2>
<div class="abs rule" style="top:1036px"><span style="left:0;width:228px;background:#ccc"></span><span style="left:0;width:30px;background:var(--accent-red)"></span><span style="left:198px;width:30px;background:var(--accent-red)"></span></div>

<div class="abs svc-photo" style="left:161px;top:1072px;width:511px;height:348px" role="img" aria-label="Photo of business people reviewing charts on a tablet"></div>
<article class="abs svc-card" style="left:641px;top:1107px;width:398px;height:280px">
  <div class="kicker">VERITAS GRID</div>
  <h3>DOC SECURE<i></i></h3>
  <p>Lorem Ipsum is simply dummy text of the printing and typesetting industry. Lorem Ipsum has been the industry's standard dummy text ever since the 1500s, when an unknown printer took a galley of type and scrambled it to make a type specimen book. It has survived not only five centuries, but also the leap into electronic typesetting, remaining essentially unchanged.</p>
  <div class="buy" style="margin-top:24px">$99 / EACH <span class="qty">1 ▾</span><span class="cart"><svg width="14" height="12" viewBox="0 0 14 12" fill="#fff"><path d="M0 0h3l1 2h10l-2 6H5z"/><circle cx="6" cy="10.5" r="1.3"/><circle cx="11" cy="10.5" r="1.3"/></svg>ADD TO CART</span></div>
</article>

<div class="abs svc-land" style="left:526px;top:1472px;width:513px;height:346px" role="img" aria-label="Photo of open farmland with mountains under a blue sky"></div>
<article class="abs svc-card" style="left:161px;top:1505px;width:398px;height:278px">
  <div class="kicker">VERITAS GRID</div>
  <h3>LAND SECURE<i></i></h3>
  <p>Lorem Ipsum is simply dummy text of the printing and typesetting industry. Lorem Ipsum has been the industry's standard dummy text ever since the 1500s, when an unknown printer took a galley of type and scrambled it to make a type specimen book. It has survived not only five centuries, but also the leap into electronic typesetting, remaining essentially unchanged.</p>
  <div class="buy" style="margin-top:24px">$99 / EACH <span class="qty">1 ▾</span><span class="cart"><svg width="14" height="12" viewBox="0 0 14 12" fill="#fff"><path d="M0 0h3l1 2h10l-2 6H5z"/><circle cx="6" cy="10.5" r="1.3"/><circle cx="11" cy="10.5" r="1.3"/></svg>ADD TO CART</span></div>
</article>

<section class="abs pricing"></section>
<h2 class="abs sec-title" style="top:1900px">PRICE</h2>
<div class="abs sub" style="top:1954px">DOC SECURE &amp; LAND SECURE</div>
<div class="abs rule" style="top:1978px"><span style="left:0;width:228px;background:var(--accent-red)"></span></div>

<article class="abs plan" style="left:161px">
  <div class="plan-head" style="background:var(--std)">STANDARD</div>
  <div class="plan-price" style="background:var(--std-soft);color:var(--std-ink)">$10<small>/mth</small></div>
  <ul>
    <li><svg width="14" height="12" viewBox="0 0 14 12"><path d="M1 6l4 4 8-9" fill="none" stroke="#d9a21a" stroke-width="2.5"/></svg>Lorem Ipsum is simply...</li>
    <li><svg width="14" height="12" viewBox="0 0 14 12"><path d="M1 6l4 4 8-9" fill="none" stroke="#d9a21a" stroke-width="2.5"/></svg>Lorem Ipsum is simply...</li>
    <li><svg width="14" height="12" viewBox="0 0 14 12"><path d="M1 6l4 4 8-9" fill="none" stroke="#d9a21a" stroke-width="2.5"/></svg>Lorem Ipsum is simply...</li>
    <li><svg width="14" height="12" viewBox="0 0 14 12"><path d="M1 6l4 4 8-9" fill="none" stroke="#d9a21a" stroke-width="2.5"/></svg>Lorem Ipsum is simply...</li>
    <li><svg width="14" height="12" viewBox="0 0 14 12"><path d="M1 6l4 4 8-9" fill="none" stroke="#d9a21a" stroke-width="2.5"/></svg>Lorem Ipsum is simply...</li>
    <li><svg width="14" height="12" viewBox="0 0 14 12"><path d="M1 6l4 4 8-9" fill="none" stroke="#d9a21a" stroke-width="2.5"/></svg>Lorem Ipsum is simply...</li>
  </ul>
  <div class="signup" style="background:var(--std)">⊕ Sign Up</div>
</article>

<article class="abs plan" style="left:472px">
  <div class="plan-head" style="background:var(--pre)">PREMIUM</div>
  <div class="plan-price" style="background:var(--pre-soft);color:#fff">$50<small>/mth</small></div>
  <ul>
    <li><svg width="14" height="12" viewBox="0 0 14 12"><path d="M1 6l4 4 8-9" fill="none" stroke="#13874c" stroke-width="2.5"/></svg>Lorem Ipsum is simply...</li>
    <li><svg width="14" height="12" viewBox="0 0 14 12"><path d="M1 6l4 4 8-9" fill="none" stroke="#13874c" stroke-width="2.5"/></svg>Lorem Ipsum is simply...</li>
    <li><svg width="14" height="12" viewBox="0 0 14 12"><path d="M1 6l4 4 8-9" fill="none" stroke="#13874c" stroke-width="2.5"/></svg>Lorem Ipsum is simply...</li>
    <li><svg width="14" height="12" viewBox="0 0 14 12"><path d="M1 6l4 4 8-9" fill="none" stroke="#13874c" stroke-width="2.5"/></svg>Lorem Ipsum is simply...</li>
    <li><svg width="14" height="12" viewBox="0 0 14 12"><path d="M1 6l4 4 8-9" fill="none" stroke="#13874c" stroke-width="2.5"/></svg>Lorem Ipsum is simply...</li>
    <li><svg width="14" height="12" viewBox="0 0 14 12"><path d="M1 6l4 4 8-9" fill="none" stroke="#13874c" stroke-width="2.5"/></svg>Lorem Ipsum is simply...</li>
  </ul>
  <div class="signup" style="background:var(--pre)">⊕ Sign Up</div>
</article>

<article class="abs plan" style="left:779px">
  <div class="plan-head" style="background:var(--adv)">ADVANCE</div>
  <div class="plan-price" style="background:var(--adv-soft);color:#fff">$70<small>/mth</small></div>
  <ul>
    <li><svg width="14" height="12" viewBox="0 0 14 12"><path d="M1 6l4 4 8-9" fill="none" stroke="#0e3457" stroke-width="2.5"/></svg>Lorem Ipsum is simply...</li>
    <li><svg width="14" height="12" viewBox="0 0 14 12"><path d="M1 6l4 4 8-9" fill="none" stroke="#0e3457" stroke-width="2.5"/></svg>Lorem Ipsum is simply...</li>
    <li><svg width="14" height="12" viewBox="0 0 14 12"><path d="M1 6l4 4 8-9" fill="none" stroke="#0e3457" stroke-width="2.5"/></svg>Lorem Ipsum is simply...</li>
    <li><svg width="14" height="12" viewBox="0 0 14 12"><path d="M1 6l4 4 8-9" fill="none" stroke="#0e3457" stroke-width="2.5"/></svg>Lorem Ipsum is simply...</li>
    <li><svg width="14" height="12" viewBox="0 0 14 12"><path d="M1 6l4 4 8-9" fill="none" stroke="#0e3457" stroke-width="2.5"/></svg>Lorem Ipsum is simply...</li>
    <li><svg width="14" height="12" viewBox="0 0 14 12"><path d="M1 6l4 4 8-9" fill="none" stroke="#0e3457" stroke-width="2.5"/></svg>Lorem Ipsum is simply...</li>
  </ul>
  <div class="signup" style="background:var(--adv)">⊕ Sign Up</div>
</article>

<footer class="abs footer"></footer>
<div class="abs contact" style="left:161px;width:268px"><span class="ico"><svg width="18" height="22" viewBox="0 0 18 22" fill="none" stroke="#fff" stroke-width="2"><path d="M9 21s-7-7-7-12a7 7 0 0114 0c0 5-7 12-7 12z"/><circle cx="9" cy="9" r="2.5"/></svg></span><span style="font-size:12px">Lorem Ipsum is simply dummy text of the printing and typesetting industry.</span></div>
<div class="abs contact" style="left:468px;width:270px"><span class="ico" style="background:#3b4a58"><svg width="20" height="20" viewBox="0 0 20 20" fill="none" stroke="#fff" stroke-width="2"><path d="M4 2l4 4-2 3c1 2 3 4 5 5l3-2 4 4-3 3C9 19 1 11 2 4z"/></svg></span>Phone: 888.555.0142</div>
<div class="abs contact" style="left:767px;width:270px"><span class="ico" style="background:#3b4a58"><svg width="22" height="16" viewBox="0 0 22 16" fill="none" stroke="#fff" stroke-width="2"><rect x="1" y="1" width="20" height="14"/><path d="M1 1l10 8 10-8"/></svg></span><span style="font-size:12px">info@veritasgrid.in</span></div>

<h4 class="abs f-h" style="left:161px">ABOUT US</h4>
<h4 class="abs f-h" style="left:565px">INFORMATION</h4>
<h4 class="abs f-h" style="left:835px">NEWSLETTER</h4>
<div class="abs f-about">Lorem Ipsum is simply dummy text of the printing and typesetting industry. Lorem Ipsum has been the industry's standard dummy text ever since the 1500s, when an unknown printer took a galley of type and scrambled it to make a type specimen book.<a>Read More »</a></div>
<ul class="abs f-links"><li>» Home</li><li>» SERVICES</li><li>» PRICING</li><li>» CONTACT US</li></ul>
<div class="abs email">Enter Your Email Id</div>
<div class="abs subscribe">SUBSCRIBE</div>
<span class="abs social" style="left:158px"></span>
<span class="abs social" style="left:195px"></span>
<span class="abs social" style="left:232px"></span>
<span class="abs social" style="left:268px"></span>
<div class="abs copy">Copyright 2017 . All Right Reserved.</div>

</body>
</html>
```